Golf Tournament Flyer and Header Needed

Non-profit needs a flyer for their benefit golf tournament - "Wild Socks Charity Golf Classic"

Target Market(s)

Design and Construction industry professionals

Industry/Entity Type

Design and Construction

Colors

Designer to choose colors to be used in the design.

Requirements
Must have
• Date: September 22, 2021, 8:00 AM Shotgun Start, Location: Briarwood Links Club. U-DorMB Logo
Nice to have
• Would like image of golfers in crazy pants incorporated.

```html
<!DOCTYPE html>
<html lang="en">
<head>
<meta charset="utf-8">
<title>Wild Socks Charity Golf Classic</title>
<link rel="stylesheet" href="https://fonts.googleapis.com/css2?family=Montserrat:wght@500;600;700;800;900&display=swap">
<style>
  :root {
    --green: #8cb43f;
    --green-light: #b5d08a;
    --blue: #1163d0;
    --ink: #4a4a4d;
    --ring: #bdbdbd;
    --paper: #ffffff;
  }
  html, body {
    margin: 0;
    padding: 0;
    width: 849px;
    height: 1200px;
    overflow: hidden;
    background: var(--paper);
  }
  .flyer {
    display: block;
    width: 849px;
    height: 1200px;
    font-family: "Montserrat", sans-serif;
  }
  .brand-name { font-weight: 600; font-size: 44px; fill: var(--ink); }
  .brand-tagline { font-weight: 500; font-size: 11px; fill: var(--green); }
  .title-wild { font-weight: 900; font-size: 220px; fill: var(--green); stroke: var(--paper); stroke-width: 10px; paint-order: stroke; }
  .title-socks { font-weight: 900; font-size: 172px; fill: var(--blue); }
  .title-classic { font-weight: 700; font-size: 48px; fill: var(--ink); }
  .info-start { font-weight: 700; font-size: 26px; fill: var(--green); }
  .info-label { font-weight: 700; font-size: 24px; fill: var(--ink); }
  .info-venue { font-weight: 800; font-size: 25px; fill: var(--blue); }
  .date-month { font-weight: 700; font-size: 24px; fill: var(--paper); }
  .date-day { font-weight: 900; font-size: 58px; fill: var(--paper); }
  .date-weekday { font-weight: 500; font-size: 23px; fill: var(--paper); }
  .date-year { font-weight: 800; font-size: 32px; fill: var(--green-light); }
</style>
</head>
<body>
<svg class="flyer" viewBox="0 0 849 1200" xmlns="http://www.w3.org/2000/svg">
  <defs>
    <linearGradient id="team-photo-tone" x1="0" y1="0" x2="0" y2="1">
      <stop offset="0" stop-color="#8fb6dc"/>
      <stop offset="0.35" stop-color="#4f7a45"/>
      <stop offset="0.6" stop-color="#e9edf2"/>
      <stop offset="1" stop-color="#3d78c9"/>
    </linearGradient>
    <linearGradient id="course-photo-tone" x1="0" y1="0" x2="0" y2="1">
      <stop offset="0" stop-color="#4f6b3c"/>
      <stop offset="1" stop-color="#8fa060"/>
    </linearGradient>
    <linearGradient id="team-pink-tone" x1="0" y1="0" x2="0" y2="1">
      <stop offset="0" stop-color="#cfe0ea"/>
      <stop offset="0.45" stop-color="#f0506e"/>
      <stop offset="1" stop-color="#5fc2b2"/>
    </linearGradient>
    <clipPath id="flyer-edge"><rect width="849" height="1200"/></clipPath>
  </defs>

  <g clip-path="url(#flyer-edge)">
    <rect class="background" width="849" height="1200" fill="var(--paper)"/>

    <!-- decorative rings -->
    <circle cx="0" cy="259" r="45" fill="none" stroke="var(--ring)" stroke-width="3"/>
    <circle cx="0" cy="837" r="46" fill="none" stroke="var(--ring)" stroke-width="3"/>
    <circle cx="849" cy="823" r="30" fill="none" stroke="var(--ring)" stroke-width="4"/>
    <circle cx="700" cy="1195" r="45" fill="none" stroke="var(--ring)" stroke-width="5"/>

    <!-- hero team photo -->
    <path class="hero-photo" role="img" aria-label="Photo of four golfers in white polos and blue-and-white argyle trousers on a course"
          d="M352 227 L669 0 L849 0 L849 583 L183 583 Q165 520 170 454 Q180 390 240 330 Z"
          fill="url(#team-photo-tone)"/>
    <circle cx="831" cy="512" r="64" fill="var(--paper)" stroke="#e6e6e6" stroke-width="12"/>

    <!-- accent bands -->
    <line x1="494" y1="62" x2="630" y2="-4" stroke="var(--green)" stroke-width="46" stroke-linecap="round"/>
    <line x1="-30" y1="650" x2="122" y2="530" stroke="var(--green)" stroke-width="74" stroke-linecap="round"/>
    <line x1="2" y1="700" x2="89" y2="640" stroke="var(--blue)" stroke-width="7" stroke-linecap="round"/>
    <line x1="764" y1="971" x2="852" y2="912" stroke="var(--blue)" stroke-width="7" stroke-linecap="round"/>

    <!-- small course photo -->
    <circle role="img" aria-label="Photo of a tree-lined fairway" cx="115" cy="371" r="46" fill="url(#course-photo-tone)"/>

    <!-- green ring right -->
    <circle cx="796" cy="677" r="50" fill="none" stroke="var(--green)" stroke-width="6"/>

    <!-- brand -->
    <g class="brand">
      <circle cx="90" cy="84" r="46" fill="var(--blue)"/>
      <text class="brand-name" x="168" y="86">U-DorMB</text>
      <line x1="168" y1="96" x2="381" y2="96" stroke="var(--ink)" stroke-width="2"/>
      <text class="brand-tagline" x="168" y="114" textLength="213" lengthAdjust="spacingAndGlyphs">Union for Design of Modern Buildings</text>
    </g>

    <!-- title -->
    <text class="title-wild" x="439" y="739" text-anchor="middle" textLength="616" lengthAdjust="spacingAndGlyphs">WILD</text>
    <text class="title-socks" x="436" y="872" text-anchor="middle" textLength="573" lengthAdjust="spacingAndGlyphs">SOCKS</text>
    <text class="title-classic" x="436" y="939" text-anchor="middle" textLength="573" lengthAdjust="spacingAndGlyphs">CHARITY GOLF CLASSIC</text>

    <!-- event details -->
    <line x1="248" y1="965" x2="643" y2="965" stroke="#d9d9d9" stroke-width="1.5"/>
    <text class="info-start" x="436" y="1004" text-anchor="middle">8:00 AM SHOTGUN START</text>
    <text class="info-label" x="436" y="1035" text-anchor="middle">LOCATION:</text>
    <text class="info-venue" x="436" y="1066" text-anchor="middle">BRIARWOOD LINKS CLUB</text>
    <line x1="248" y1="1082" x2="643" y2="1082" stroke="#d9d9d9" stroke-width="1.5"/>

    <!-- date badge -->
    <circle cx="119" cy="1102" r="144" fill="none" stroke="var(--blue)" stroke-width="1.2" stroke-dasharray="4 3"/>
    <circle cx="119" cy="1102" r="137" fill="var(--green)"/>
    <text class="date-month" x="28" y="1027" textLength="173" lengthAdjust="spacingAndGlyphs">SEPTEMBER</text>
    <text class="date-day" x="26" y="1072" textLength="184" lengthAdjust="spacingAndGlyphs">22ND</text>
    <text class="date-weekday" x="29" y="1115" textLength="172" lengthAdjust="spacingAndGlyphs">WEDNESDAY</text>
    <text class="date-year" x="33" y="1150">2021</text>

    <!-- bottom ring -->
    <circle cx="290" cy="1196" r="48" fill="none" stroke="var(--green)" stroke-width="6"/>

    <!-- second team photo -->
    <circle role="img" aria-label="Photo of four golfers in coral polos and tropical-print trousers" cx="765" cy="1110" r="123" fill="url(#team-pink-tone)"/>
  </g>
</svg>
</body>
</html>
```